Website redesign for job agency recruitment

Please refer to the attached document, “Harbor Work Portal Outline,” for comprehensive details regarding the scope, objectives, and requirements of this website redesign project.

For imagery you can use images from this website https://www.pixvaultmedia.com or any other you regularly use.

Target Market(s)

Jobseekers and Companies looking for general labour

Industry/Entity Type

Services: Oil, Gas and Mining, Administrative, Construction and Trades, Warehouse and Logistics and, Manufacturing.

Number of Pages Required

5+ page

Font styles to use
Serif
Other font styles liked:
• Inter, Open-Sans or similar.

Requirements
Must have
• The requirements highlighted in the Word document attached. The final design needs to be provided in Figma including all viewports (Desktop, mobiel and tablet)
Should not have
• Website we like as a reference: www.beltonworkforceinc.com, www.veltaworkforce.com, www.zplacer.com, www.brimwellworkforce.com, www.9tworkcrew.com, www.hiringonthemove.ca

```html
<!DOCTYPE html>
<html lang="en">
<head>
<meta charset="utf-8">
<title>Harbor Work Agency — Recruitment</title>
<link href="https://fonts.googleapis.com/css2?family=Inter:wght@400;500;600;700&family=Plus+Jakarta+Sans:wght@600;700;800&display=swap" rel="stylesheet">
<style>
:root{
  --navy:#1f2a6e;
  --navy-deep:#18225c;
  --gold:#fbbf24;
  --gold-soft:#fde8a6;
  --ink:#1f2a6e;
  --text:#5b6275;
  --muted:#8a90a2;
  --line:#e3e6ef;
  --bg-soft:#f6f7fb;
  --white:#ffffff;
}
*{box-sizing:border-box;margin:0;padding:0}
html,body{width:1200px;height:3591px;overflow:hidden}
body{font-family:'Inter',sans-serif;color:var(--text);background:var(--white);position:relative}
h1,h2,h3,.display{font-family:'Plus Jakarta Sans',sans-serif;color:var(--ink)}
.abs{position:absolute}
svg{display:block}

/* nav */
.site-nav{position:absolute;top:0;left:0;width:1200px;height:63px;background:#eeeff2;display:flex;align-items:center;z-index:5}
.brand{position:absolute;left:220px;top:14px;display:flex;align-items:center;gap:6px;font-weight:700;font-size:14px;color:var(--navy)}
.brand .dot{width:14px;height:14px;border-radius:50%;background:var(--gold)}
.nav-links{position:absolute;left:595px;top:0;height:63px;display:flex;align-items:center;gap:22px;font-size:10.5px;color:var(--navy);font-weight:500}
.btn{display:inline-flex;align-items:center;justify-content:center;gap:7px;border-radius:5px;font-weight:600;font-family:'Inter',sans-serif}
.nav-find{position:absolute;left:831px;top:18px;width:72px;height:27px;background:var(--gold);color:var(--navy);font-size:10px}
.nav-hire{position:absolute;left:924px;top:18px;width:76px;height:27px;background:var(--navy);color:#fff;font-size:10px}

/* hero */
.hero{position:absolute;top:63px;left:0;width:1200px;height:524px;background:linear-gradient(100deg,#2a3558 0%,#3a4a6c 40%,#5a6479 70%,#7b6a62 100%)}
.hero h1{position:absolute;left:200px;top:132px;font-size:42px;line-height:41px;color:#fff;font-weight:700;width:420px}
.hero p{position:absolute;left:200px;top:227px;font-size:13px;line-height:19px;color:#dfe3ee;width:400px}
.hero .btn-cand{position:absolute;left:200px;top:290px;width:161px;height:39px;background:var(--gold);color:var(--navy);font-size:11px}
.hero .btn-emp{position:absolute;left:372px;top:290px;width:159px;height:39px;border:1px solid rgba(255,255,255,.5);background:rgba(255,255,255,.08);color:#fff;font-size:11px}

.stats{position:absolute;left:275px;top:545px;width:650px;height:85px;background:var(--navy);border-radius:8px;display:flex;box-shadow:0 12px 26px rgba(31,42,110,.25);z-index:3}
.stat{flex:1;text-align:center;padding-top:20px;border-right:1px solid rgba(255,255,255,.12)}
.stat:last-child{border-right:none}
.stat b{display:block;font-family:'Plus Jakarta Sans',sans-serif;font-size:25px;color:var(--gold);line-height:26px}
.stat span{font-size:9.5px;color:#d9ddf0}

.eyebrow{font-size:9px;letter-spacing:1.4px;font-weight:700;color:#c9960f;text-transform:uppercase}
.center{text-align:center;width:1200px;left:0}

/* accordion */
.acc{position:absolute;left:258px;width:683px;border:1px solid var(--line);border-radius:8px;background:#fff}
.acc.open{border-color:#c9cde3;box-shadow:0 4px 14px rgba(31,42,110,.08)}
.num{position:absolute;left:17px;width:32px;height:32px;border-radius:6px;background:#eef0f8;color:var(--navy);font-weight:700;font-size:12px;display:flex;align-items:center;justify-content:center}
.acc.open .num{background:var(--gold)}
.acc h3{position:absolute;left:62px;font-family:'Inter',sans-serif;font-size:12.5px;font-weight:600}
.acc .sub{position:absolute;left:62px;font-size:9px;color:var(--muted)}
.chev{position:absolute;right:18px}
.check-list{list-style:none;position:absolute;left:298px;top:112px;font-size:9px;color:var(--text)}
.check-list li{display:flex;align-items:center;gap:9px;height:22.5px}

/* sector cards */
.sector-card{position:absolute;top:1714px;width:151px;height:172px;border-radius:7px;overflow:hidden}
.sector-card .label{position:absolute;left:13px;bottom:14px;right:10px;color:#fff}
.sector-card b{display:block;font-size:11px;font-weight:600;margin-bottom:3px}
.sector-card span{font-size:8px;line-height:12px;color:#d8dbe6;display:block}

.feature{position:absolute;left:200px;width:380px}
.feature .tick{position:absolute;left:0;top:2px;width:20px;height:20px;border-radius:5px;background:#fdf1cf;display:flex;align-items:center;justify-content:center}
.feature b{display:block;margin-left:32px;font-size:10.5px;color:var(--navy);font-weight:600}
.feature span{display:block;margin-left:32px;margin-top:3px;font-size:8.5px;line-height:14px;color:var(--muted)}

/* contact */
.contact-row{position:absolute;left:200px;display:flex;gap:12px;font-size:9px}
.contact-row .ic{width:32px;height:32px;border-radius:6px;background:#eef0f8;display:flex;align-items:center;justify-content:center}
.contact-row b{display:block;color:var(--navy);font-weight:600;font-size:9.5px;margin-top:3px}
.form{position:absolute;left:622px;top:2867px;width:378px;height:411px;border:1px solid var(--line);border-radius:8px;background:#fff}
.field{position:absolute;font-size:7.5px;color:var(--navy);font-weight:500}
.field .in{margin-top:6px;height:29px;border:1px solid var(--line);border-radius:4px;font-size:9px;color:#a6abbb;padding:9px 11px;font-weight:400}
.req{color:#e0524b}

/* footer */
.footer{position:absolute;top:3353px;left:0;width:1200px;height:238px;background:var(--navy-deep)}
.fcol{position:absolute;top:49px;font-size:9px;color:#aeb4d2}
.fcol h4{font-size:9px;letter-spacing:1.2px;color:var(--gold);font-weight:700;margin-bottom:16px}
.fcol li{list-style:none;margin-bottom:12px}
</style>
</head>
<body>

<nav class="site-nav">
  <div class="brand"><span class="dot"></span>HWA</div>
  <div class="nav-links"><span>Services</span><span>Sectors</span><span>About Us</span><span>Contact</span></div>
  <a class="btn nav-find">Find a Job</a>
  <a class="btn nav-hire">Hire Talent</a>
</nav>

<header class="hero" role="img" aria-label="Office boardroom overlooking a city skyline at dusk">
  <h1>Your Future Starts Here</h1>
  <p>Thousands of opportunities across the nation — let us help you take the next step in your career.</p>
  <a class="btn btn-cand"><svg width="12" height="12" viewBox="0 0 24 24" fill="none" stroke="#1f2a6e" stroke-width="2"><circle cx="12" cy="8" r="4"/><path d="M4 21c1-4 4-6 8-6s7 2 8 6"/></svg>For Candidates<svg width="11" height="11" viewBox="0 0 24 24" fill="none" stroke="#1f2a6e" stroke-width="2.4"><path d="M5 12h14M13 6l6 6-6 6"/></svg></a>
  <a class="btn btn-emp"><svg width="12" height="12" viewBox="0 0 24 24" fill="none" stroke="#fff" stroke-width="2"><rect x="5" y="3" width="14" height="18"/><path d="M9 7h2M13 7h2M9 11h2M13 11h2M9 15h2M13 15h2"/></svg>For Employers<svg width="11" height="11" viewBox="0 0 24 24" fill="none" stroke="#fff" stroke-width="2.4"><path d="M5 12h14M13 6l6 6-6 6"/></svg></a>
</header>

<div class="stats">
  <div class="stat"><b>12,000+</b><span>Placements Made</span></div>
  <div class="stat"><b>850+</b><span>Client Companies</span></div>
  <div class="stat"><b>25+</b><span>Years Experience</span></div>
  <div class="stat"><b>98%</b><span>Client Satisfaction</span></div>
</div>

<!-- sectors -->
<div class="abs center eyebrow" style="top:716px">Our Sectors</div>
<h2 class="abs center" style="top:732px;font-size:33px;font-weight:700">Industries We Recruit For</h2>
<p class="abs" style="top:780px;left:380px;width:440px;text-align:center;font-size:12px;line-height:19px">Deep sector expertise across the industries that power the economy — we supply qualified, vetted candidates where they're needed most.</p>

<div class="acc open" style="top:861px;height:269px">
  <div class="num" style="top:16px">01</div>
  <h3 style="top:24px">Oil, Gas &amp; Mining</h3>
  <svg class="chev" style="top:26px" width="12" height="12" viewBox="0 0 24 24" fill="none" stroke="#8a90a2" stroke-width="2"><path d="M6 15l6-6 6 6"/></svg>
  <div class="abs" role="img" aria-label="Drilling rig on a desert mining landscape" style="left:17px;top:64px;width:260px;height:170px;border-radius:5px;background:linear-gradient(180deg,#5d8fc8 0%,#9cc0e2 45%,#b89470 55%,#7e5e40 100%)"></div>
  <p class="abs" style="left:298px;top:68px;width:370px;font-size:10.5px;line-height:17px">Specialist recruitment for upstream, downstream and mining operations — from roustabouts to project managers.</p>
  <ul class="check-list">
    <li><svg width="11" height="11" viewBox="0 0 24 24" fill="none" stroke="#e0a915" stroke-width="3"><path d="M4 12l5 5 11-11"/></svg>Skilled trades and technical operators for rigs, refineries and mine sites</li>
    <li><svg width="11" height="11" viewBox="0 0 24 24" fill="none" stroke="#e0a915" stroke-width="3"><path d="M4 12l5 5 11-11"/></svg>FIFO and remote-site workforce mobilisation</li>
    <li><svg width="11" height="11" viewBox="0 0 24 24" fill="none" stroke="#e0a915" stroke-width="3"><path d="M4 12l5 5 11-11"/></svg>HSE-qualified candidates with valid safety certifications</li>
    <li><svg width="11" height="11" viewBox="0 0 24 24" fill="none" stroke="#e0a915" stroke-width="3"><path d="M4 12l5 5 11-11"/></svg>Shutdown, turnaround and project-based labour hire</li>
    <li><svg width="11" height="11" viewBox="0 0 24 24" fill="none" stroke="#e0a915" stroke-width="3"><path d="M4 12l5 5 11-11"/></svg>Compliance with industry-specific regulations and right-to-work requirements</li>
  </ul>
  <a class="abs" style="left:298px;top:234px;font-size:9px;font-weight:600;color:var(--navy);display:flex;gap:6px;align-items:center">Learn more <svg width="10" height="10" viewBox="0 0 24 24" fill="none" stroke="#1f2a6e" stroke-width="2.4"><path d="M5 12h14M13 6l6 6-6 6"/></svg></a>
</div>

<div class="acc" style="top:1143px;height:64px"><div class="num" style="top:16px">02</div><h3 style="top:17px">Administrative</h3><div class="sub" style="top:37px">Professional office and admin staff to keep your business running smoothly — temporary, contract and permanent.</div><svg class="chev" style="top:26px" width="12" height="12" viewBox="0 0 24 24" fill="none" stroke="#8a90a2" stroke-width="2"><path d="M6 9l6 6 6-6"/></svg></div>
<div class="acc" style="top:1220px;height:64px"><div class="num" style="top:16px">03</div><h3 style="top:17px">Construction &amp; Trades</h3><div class="sub" style="top:37px">Reliable tradespeople and construction professionals for projects of every scale.</div><svg class="chev" style="top:26px" width="12" height="12" viewBox="0 0 24 24" fill="none" stroke="#8a90a2" stroke-width="2"><path d="M6 9l6 6 6-6"/></svg></div>
<div class="acc" style="top:1297px;height:64px"><div class="num" style="top:16px">04</div><h3 style="top:17px">Warehouse &amp; Logistics</h3><div class="sub" style="top:37px">Scalable warehouse and supply-chain staffing to meet peak demand and daily operations.</div><svg class="chev" style="top:26px" width="12" height="12" viewBox="0 0 24 24" fill="none" stroke="#8a90a2" stroke-width="2"><path d="M6 9l6 6 6-6"/></svg></div>
<div class="acc" style="top:1374px;height:64px"><div class="num" style="top:16px">05</div><h3 style="top:17px">Manufacturing</h3><div class="sub" style="top:37px">Production-ready candidates for assembly lines, quality control and engineering-led manufacturing environments.</div><svg class="chev" style="top:26px" width="12" height="12" viewBox="0 0 24 24" fill="none" stroke="#8a90a2" stroke-width="2"><path d="M6 9l6 6 6-6"/></svg></div>

<!-- overview -->
<section class="abs" style="top:1525px;left:0;width:1200px;height:435px;background:var(--bg-soft)"></section>
<div class="abs center eyebrow" style="top:1603px">At a Glance</div>
<h2 class="abs center" style="top:1620px;font-size:25px;font-weight:700">Sectors We Cover</h2>
<p class="abs center" style="top:1661px;font-size:11px">Click any sector above for full details, or browse the overview below.</p>

<div class="sector-card" style="left:200px;background:linear-gradient(180deg,#5d8fc8 0%,#9a8466 55%,#2c2e3e 100%)" role="img" aria-label="Oil rig in a desert landscape"><div class="label"><b>Oil, Gas &amp; Mining</b><span>Specialist recruitment for upstream, downstream and...</span></div></div>
<div class="sector-card" style="left:362px;background:linear-gradient(180deg,#e6e6e6 0%,#9b9da3 55%,#2c2e3e 100%)" role="img" aria-label="Laptop on an office desk"><div class="label"><b>Administrative</b><span>Professional office and admin staff to keep your business...</span></div></div>
<div class="sector-card" style="left:524px;background:linear-gradient(180deg,#d79a7c 0%,#7a7f8a 55%,#2c2e3e 100%)" role="img" aria-label="Construction crane against the sky"><div class="label"><b>Construction &amp; Trades</b><span>Reliable tradespeople and construction professionals for...</span></div></div>
<div class="sector-card" style="left:687px;background:linear-gradient(180deg,#9aa6b8 0%,#5d6a80 55%,#2c2e3e 100%)" role="img" aria-label="Warehouse aisles with racking"><div class="label"><b>Warehouse &amp; Logistics</b><span>Scalable warehouse and supply-chain staffing to meet peak...</span></div></div>
<div class="sector-card" style="left:849px;background:linear-gradient(180deg,#5f86bf 0%,#3f5580 55%,#22294a 100%)" role="img" aria-label="Factory production floor"><div class="label"><b>Manufacturing</b><span>Production-ready candidates for assembly lines, quality control...</span></div></div>

<!-- why choose us -->
<div class="abs eyebrow" style="top:2037px;left:200px">Why Choose Us</div>
<h2 class="abs" style="top:2056px;left:200px;width:400px;font-size:25px;line-height:27px;font-weight:700">A Recruitment Partner You Can Trust</h2>
<p class="abs" style="top:2126px;left:200px;width:380px;font-size:11.5px;line-height:19.5px">With over 25 years of experience, Harbor Work Agency has built a reputation for delivering exceptional recruitment solutions. We combine industry expertise with a personal approach to ensure every placement is the right fit.</p>
<div class="feature" style="top:2226px"><div class="tick"><svg width="10" height="10" viewBox="0 0 24 24" fill="none" stroke="#e0a915" stroke-width="3"><path d="M4 12l5 5 11-11"/></svg></div><b>Dedicated Consultants</b><span>Every client gets a named consultant who understands your industry, culture and hiring needs.</span></div>
<div class="feature" style="top:2287px"><div class="tick"><svg width="10" height="10" viewBox="0 0 24 24" fill="none" stroke="#e0a915" stroke-width="3"><path d="M4 12l5 5 11-11"/></svg></div><b>Nationwide Coverage</b><span>From major cities to regional towns — we have the network to source talent wherever you need it.</span></div>
<div class="feature" style="top:2348px"><div class="tick"><svg width="10" height="10" viewBox="0 0 24 24" fill="none" stroke="#e0a915" stroke-width="3"><path d="M4 12l5 5 11-11"/></svg></div><b>Speed &amp; Quality</b><span>Our rigorous screening process means you get high-quality candidates, fast.</span></div>
<div class="feature" style="top:2394px"><div class="tick"><svg width="10" height="10" viewBox="0 0 24 24" fill="none" stroke="#e0a915" stroke-width="3"><path d="M4 12l5 5 11-11"/></svg></div><b>Full Compliance</b><span>All workers are fully vetted, right-to-work checked and compliant with industry regulations.</span></div>

<div class="abs" role="img" aria-label="Person working on a laptop at a white desk, viewed from above" style="left:622px;top:2077px;width:378px;height:320px;border-radius:8px;background:linear-gradient(135deg,#2d2f36 0%,#e9e9e9 35%,#f2f2f2 65%,#3a3b40 100%)"></div>
<div class="abs" style="left:605px;top:2328px;width:148px;height:85px;border-radius:7px;background:var(--navy);padding:16px 17px;box-shadow:0 10px 22px rgba(31,42,110,.3)">
  <div class="display" style="font-size:20px;color:var(--gold);font-weight:700;line-height:20px">25+</div>
  <div style="font-size:9px;line-height:13px;color:#d9ddf0;margin-top:5px">Years of trusted recruitment excellence</div>
</div>

<!-- CTA -->
<section class="abs" style="top:2514px;left:0;width:1200px;height:278px;background:linear-gradient(100deg,#28336f 0%,var(--navy) 45%,#24307a 100%)"></section>
<h2 class="abs center" style="top:2574px;font-size:32px;color:#fff;font-weight:700">Ready to Take the Next Step?</h2>
<p class="abs" style="top:2625px;left:370px;width:460px;text-align:center;font-size:12px;line-height:19px;color:#c3c8e2">Whether you're looking for your next career move or searching for top talent — we're here to help.</p>
<a class="btn abs" style="left:432px;top:2689px;width:167px;height:37px;background:var(--gold);color:var(--navy);font-size:11px">I'm Looking for a Job <svg width="11" height="11" viewBox="0 0 24 24" fill="none" stroke="#1f2a6e" stroke-width="2.4"><path d="M5 12h14M13 6l6 6-6 6"/></svg></a>
<a class="btn abs" style="left:610px;top:2689px;width:157px;height:37px;border:1px solid rgba(255,255,255,.45);color:#fff;font-size:11px">I Need to Hire Staff <svg width="11" height="11" viewBox="0 0 24 24" fill="none" stroke="#fff" stroke-width="2.4"><path d="M5 12h14M13 6l6 6-6 6"/></svg></a>

<!-- contact -->
<section class="abs" style="top:2792px;left:0;width:1200px;height:561px;background:var(--bg-soft)"></section>
<div class="abs eyebrow" style="top:2866px;left:200px">Get in Touch</div>
<h2 class="abs" style="top:2885px;left:200px;font-size:25px;font-weight:700">Let's Start a Conversation</h2>
<p class="abs" style="top:2931px;left:200px;width:380px;font-size:11.5px;line-height:19.5px">Whether you're a candidate or an employer, our team is ready to help. Fill out the form and one of our consultants will be in touch within 24 hours.</p>
<div class="contact-row" style="top:3016px"><div class="ic"><svg width="13" height="13" viewBox="0 0 24 24" fill="none" stroke="#1f2a6e" stroke-width="2"><path d="M5 3h4l2 5-3 2a12 12 0 0 0 6 6l2-3 5 2v4a2 2 0 0 1-2 2A18 18 0 0 1 3 5a2 2 0 0 1 2-2z"/></svg></div><div><b>Phone</b>0800 555 0192</div></div>
<div class="contact-row" style="top:3064px"><div class="ic"><svg width="13" height="13" viewBox="0 0 24 24" fill="none" stroke="#1f2a6e" stroke-width="2"><rect x="3" y="5" width="18" height="14" rx="2"/><path d="M3 7l9 6 9-6"/></svg></div><div><b>Email</b>info@harborworkagency.com</div></div>
<div class="contact-row" style="top:3112px"><div class="ic"><svg width="13" height="13" viewBox="0 0 24 24" fill="none" stroke="#1f2a6e" stroke-width="2"><path d="M12 21s-7-6-7-11a7 7 0 0 1 14 0c0 5-7 11-7 11z"/><circle cx="12" cy="10" r="2.5"/></svg></div><div><b>Office</b>Harbor House, 48 Quayside Park, Leeds, LS1 4AP</div></div>

<div class="form">
  <div class="field" style="left:21px;top:22px;width:163px">First Name <span class="req">*</span><div class="in">John</div></div>
  <div class="field" style="left:194px;top:22px;width:163px">Last Name <span class="req">*</span><div class="in">Smith</div></div>
  <div class="field" style="left:21px;top:81px;width:335px">Email <span class="req">*</span><div class="in">john@company.com</div></div>
  <div class="field" style="left:21px;top:140px;width:335px">Phone<div class="in">07123 456 789</div></div>
  <div class="field" style="left:21px;top:199px;width:335px">I am a... <span class="req">*</span><div class="in" style="color:var(--navy);display:flex;justify-content:space-between">Please select... <svg width="9" height="9" viewBox="0 0 24 24" fill="none" stroke="#1f2a6e" stroke-width="2.4"><path d="M6 9l6 6 6-6"/></svg></div></div>
  <div class="field" style="left:21px;top:258px;width:335px">Message<div class="in" style="height:70px">Tell us how we can help...</div></div>
  <div class="abs btn" style="left:21px;top:358px;width:335px;height:31px;background:var(--gold-soft);color:#c7a24a;font-size:9.5px">Send Enquiry</div>
</div>

<!-- footer -->
<footer class="footer">
  <div class="abs" style="left:200px;top:46px;display:flex;align-items:center;gap:6px;color:#fff;font-weight:700;font-size:13px"><span style="width:12px;height:12px;border-radius:50%;background:var(--gold)"></span>HWA</div>
  <p class="abs" style="left:200px;top:85px;width:190px;font-size:9px;line-height:15px;color:#aeb4d2">Your trusted national recruitment partner connecting talent with opportunity.</p>
  <div class="fcol" style="left:407px"><h4>QUICK LINKS</h4><ul><li>Services</li><li>Sectors</li><li>About Us</li><li>Contact</li></ul></div>
  <div class="fcol" style="left:613px"><h4>CANDIDATES</h4><ul><li>Browse Jobs</li><li>Submit CV</li><li>How It Works</li></ul></div>
  <div class="fcol" style="left:820px"><h4>EMPLOYERS</h4><ul><li>Hire Staff</li><li>Solutions</li><li>Testimonials</li></ul></div>
  <div class="abs" style="left:200px;top:190px;width:800px;border-top:1px solid rgba(255,255,255,.1)"></div>
  <div class="abs" style="left:200px;top:206px;font-size:7.5px;color:#8f96bb">© 2026 Harbor Work Agency. All rights reserved.</div>
  <div class="abs" style="left:799px;top:206px;font-size:7.5px;color:#8f96bb;display:flex;gap:16px"><span>Privacy Policy</span><span>Terms of Service</span><span>Cookie Policy</span></div>
</footer>

</body>
</html>
```